I need a logo that demonstrates multiple of the same with one of a distinguishing feature. I would like something that can be recognisable in silhouette format. The business designs Management systems bespoke the to the company helping them pre-qualify for work.
Something that can demonstrate a distinction between a collective group non of which are the same in shape or size, with the largest of these not the distinguished object (or something to that effect).
This is a new business no logo or artwork exists.
Target Market(s)
Small to Medium Size enterprises in the city and rural areas. Looking to make the step up.
Industry/Entity Type
Manufacture
Contact Information for Business Card
room for, Name, Email, phone number
Font styles to use
Requirements
Must have
- would like the silhouette to be recognisable
Nice to have
- would like it to incorporate the name Quarrywell Advisory Systems.
- Would like the same logo to be on both business cards and on corporate shirts
Should not have
- anything that may exclude rural trade or manufacturing.
- I don't want to appear as corporate, just professional

```html
<!DOCTYPE html>
<html lang="en">
<head>
<meta charset="utf-8">
<title>Quarrywell Advisory Systems – Business Card</title>
<link href="https://fonts.googleapis.com/css2?family=Source+Sans+3:wght@400;600&display=swap" rel="stylesheet">
<style>
  :root {
    --brand-red: #e8232a;
    --brand-red-deep: #c91c22;
    --ink: #2b2b2b;
    --paper: #ffffff;
    --stage-top: #2a2a2a;
    --stage-bottom: #0b0b0b;
  }
  html, body {
    margin: 0;
    padding: 0;
    overflow: hidden;
  }
  body {
    width: 1200px;
    height: 900px;
    position: relative;
    background: linear-gradient(to bottom, var(--stage-top), var(--stage-bottom));
    font-family: "Source Sans 3", "Segoe UI", sans-serif;
  }
  .card {
    position: absolute;
    top: 170px;
    width: 347px;
    height: 561px;
    box-sizing: border-box;
  }
  .card--front {
    left: 259px;
    background: var(--paper);
    text-align: center;
    color: var(--ink);
  }
  .card--back {
    left: 631px;
    background: var(--brand-red);
  }
  .accent-band {
    position: absolute;
    left: 102px;
    width: 143px;
    background: var(--brand-red);
  }
  .accent-band--top { top: 0; height: 30px; }
  .accent-band--bottom { bottom: 0; height: 28px; }

  .brand {
    position: absolute;
    top: 100px;
    left: 0;
    right: 0;
    color: var(--brand-red);
    font-weight: 600;
  }
  .brand__dot {
    display: block;
    width: 58px;
    height: 58px;
    margin: 0 auto 14px;
    border-radius: 50%;
    background: var(--brand-red);
  }
  .brand__name {
    font-size: 33px;
    line-height: 1;
    letter-spacing: 1.5px;
    text-transform: uppercase;
  }
  .brand__tagline {
    font-size: 22px;
    line-height: 1.2;
    margin-top: 4px;
  }

  .person {
    position: absolute;
    top: 276px;
    left: 0;
    right: 0;
  }
  .person__name {
    color: var(--brand-red);
    font-size: 26px;
    font-weight: 400;
    line-height: 1;
    margin: 0;
  }
  .person__role {
    font-size: 15px;
    margin-top: 7px;
  }

  .contact {
    position: absolute;
    top: 349px;
    left: 0;
    right: 0;
    font-size: 15px;
    line-height: 21px;
  }
  .contact__row {
    display: flex;
    justify-content: center;
    align-items: center;
    gap: 9px;
  }
  .contact__icon {
    width: 11px;
    height: 11px;
    fill: var(--brand-red);
  }

  .address {
    position: absolute;
    top: 465px;
    left: 0;
    right: 0;
    font-size: 15px;
    line-height: 18px;
  }

  .back-mark {
    position: absolute;
    top: 170px;
    left: 0;
    right: 0;
    text-align: center;
    color: var(--brand-red-deep);
    font-weight: 600;
  }
  .back-mark__ring {
    display: block;
    width: 200px;
    height: 200px;
    margin: 0 auto 22px;
    border-radius: 50%;
    border: 2px solid var(--brand-red-deep);
    box-sizing: border-box;
  }
  .back-mark__name {
    font-size: 22px;
    letter-spacing: 1.5px;
    text-transform: uppercase;
  }
</style>
</head>
<body>

  <section class="card card--front" aria-label="Business card front">
    <div class="accent-band accent-band--top"></div>

    <div class="brand">
      <span class="brand__dot" aria-hidden="true"></span>
      <div class="brand__name">Quarrywell</div>
      <div class="brand__tagline">Advisory Systems</div>
    </div>

    <div class="person">
      <h1 class="person__name">MARTIN HALE</h1>
      <div class="person__role">Managing Director</div>
    </div>

    <div class="contact">
      <div class="contact__row">
        <svg class="contact__icon" viewBox="0 0 12 12" aria-hidden="true">
          <path d="M1 4.5C1 2.5 3 1.5 6 1.5S11 2.5 11 4.5L8.5 4.8 8.2 3.6H3.8L3.5 4.8Z M3 6h6l1.5 4.5h-9Z"/>
        </svg>
        <span>823-555-0147</span>
      </div>
      <div class="contact__row">
        <svg class="contact__icon" viewBox="0 0 12 12" aria-hidden="true">
          <path d="M0.5 2.5h11v7h-11Z M1.5 3.2 6 6.6 10.5 3.2" fill="var(--brand-red)" stroke="#fff" stroke-width="0.9"/>
        </svg>
        <span>info@quarrywell.com</span>
      </div>
    </div>

    <div class="address">
      1234, Address Goes Here<br>
      Country Name, 123456
    </div>

    <div class="accent-band accent-band--bottom"></div>
  </section>

  <section class="card card--back" aria-label="Business card back">
    <div class="back-mark">
      <span class="back-mark__ring" aria-hidden="true"></span>
      <div class="back-mark__name">Quarrywell</div>
    </div>
  </section>

</body>
</html>
```